Website design needed for Renewable utilities company based in New Zealand.

Website design needed for Tarnwick Collective based in New Zealand.

Please see attached logo.

We sell solar panels, vertical axis wind turbines, atmospheric water generators and other related equipment for those who don't have access or don't want to depend on the government, city councils for their utilities (power and water).

We like metallic texture, dark grey and purple, red or blue colours. The design should go well with the attached logo.

Target Market(s)

The Eco conscious

Industry/Entity Type

Government

Logo Text

Tarnwick Horizon

Requirements
Must have
• Must Have:
- Metallic finish is a must.
- Design should fit around the attached logo well.
Nice to have
• Sharpe design prefred rather than rounded edges

```html
<!DOCTYPE html>
<html lang="en">
<head>
<meta charset="utf-8">
<title>Tarnwick Horizon – Home</title>
<link href="https://fonts.googleapis.com/css2?family=Arimo:wght@400;700&display=swap" rel="stylesheet">
<style>
:root{
  --blue:#1a86c8;
  --blue-dark:#0f6aa6;
  --blue-text:#1b7dc0;
  --ink:#1a1a1a;
  --grey-text:#6a6a6a;
  --rule:#d6d6d6;
  --footer-bg:#030303;
  --footer-text:#4c4c4c;
  --white:#ffffff;
  --hero-tone:#8fa6bd;
  --inset-tone:#7d9cbf;
  --product-tone:#e9ecf0;
}
*{box-sizing:border-box;margin:0;padding:0}
html,body{width:837px;height:1200px;overflow:hidden}
body{
  position:relative;
  font-family:"Arimo",Arial,sans-serif;
  color:var(--ink);
  background:
    repeating-linear-gradient(90deg,rgba(255,255,255,.05) 0 1px,transparent 1px 3px,rgba(0,0,0,.18) 3px 4px,transparent 4px 7px),
    linear-gradient(90deg,#1c1c1c,#3b3b3b 20%,#2a2a2a 50%,#404040 78%,#1e1e1e);
}
.abs{position:absolute}

/* Header */
.site-header{left:79px;top:14px;width:679px;height:84px;background:linear-gradient(#ffffff,#e4e4e4);border-top:3px solid var(--blue);box-shadow:0 2px 6px rgba(0,0,0,.5)}
.brand{left:14px;top:10px;width:120px;text-align:center}
.brand-mark{display:block;width:40px;height:40px;margin:0 auto 6px;border-radius:50%;background:var(--blue-dark)}
.brand-name{font-size:14px;color:var(--blue-dark);white-space:nowrap}
.contact-bar{right:16px;top:21px;font-size:8.5px;color:#555;display:flex;align-items:center;gap:10px}
.contact-bar svg{vertical-align:middle;margin-right:3px}
.social-dot{display:inline-block;width:11px;height:11px;border-radius:50%;background:#8c8c8c;margin-left:2px}
.main-nav{right:12px;top:49px;display:flex;gap:3px}
.main-nav a{display:block;height:19px;line-height:19px;padding:0 12px;font-size:9.5px;color:#fff;text-decoration:none;background:linear-gradient(#b0b0b0,#8a8a8a);border:1px solid #7c7c7c}
.main-nav a.is-active{background:linear-gradient(#2da0e0,#1279bb);border-color:#0f6aa6}

/* Hero slider */
.hero{left:79px;top:117px;width:679px;height:364px;box-shadow:0 6px 14px rgba(0,0,0,.6)}
.hero-photo{width:100%;height:100%;background:var(--hero-tone)}
.hero-arrow{top:163px;width:39px;height:38px;background:rgba(40,40,40,.8);display:flex;align-items:center;justify-content:center}
.hero-arrow.prev{left:8px}
.hero-arrow.next{right:8px}
.hero-dots{left:308px;top:344px;display:flex;gap:3px}
.hero-dots span{width:11px;height:11px;border-radius:50%;background:#e6e6e6;border:1px solid #bbb}
.hero-dots span.is-current{background:var(--blue);border-color:var(--blue-dark)}

/* Content panel */
.content-panel{left:79px;top:518px;width:679px;height:522px;background:var(--white);border-top:5px solid var(--blue)}
.section-title{font-size:15px;font-weight:400;color:var(--blue-text)}
.welcome{left:26px;top:34px;width:246px}
.welcome p{font-size:7.6px;line-height:11px;margin-top:8px}
.welcome p + p{margin-top:11px}
.btn-primary{display:inline-block;margin-top:10px;height:18px;line-height:18px;padding:0 7px;font-size:8px;font-weight:700;color:#fff;background:linear-gradient(#2da0e0,#1279bb);border:1px solid #0f6aa6;box-shadow:0 1px 2px rgba(0,0,0,.3)}
.welcome-photo{left:280px;top:56px;width:143px;height:154px;background:var(--inset-tone)}
.col-divider{left:458px;top:20px;width:1px;height:214px;background:var(--rule)}
.news{left:493px;top:47px;width:172px}
.news-item{margin-top:10px;padding-bottom:7px;border-bottom:1px dashed #c8c8c8}
.news-item:last-child{border-bottom:0}
.news-date{font-size:7.5px;color:var(--blue-text)}
.news-head{font-size:7.5px;font-weight:700;margin-top:8px;line-height:9px}
.news-body{font-size:7px;color:var(--grey-text);line-height:9.5px;margin-top:9px}
.news-more{display:block;text-align:right;font-size:7.5px;color:var(--blue-text);margin-top:2px;padding-right:8px}
.row-divider{left:22px;top:255px;width:635px;height:1px;background:var(--rule)}
.products-title{left:26px;top:280px}
.product-list{left:26px;top:309px;display:flex;gap:14px}
.product-card{width:114px;height:171px;background:#fff;border-bottom:3px solid #222;box-shadow:0 1px 4px rgba(0,0,0,.3);text-align:center}
.product-name{height:20px;line-height:20px;font-size:10px;color:#fff;background:linear-gradient(#2da0e0,#1279bb)}
.product-photo{width:70px;height:96px;margin:8px auto 0;background:var(--product-tone)}
.product-price{font-size:7.5px;margin-top:9px}
.btn-cart{display:inline-flex;align-items:center;margin-top:5px;height:18px;font-size:7.5px;color:#fff;background:linear-gradient(#2da0e0,#1279bb);border:1px solid #0f6aa6}
.btn-cart .icon{width:18px;height:16px;display:flex;align-items:center;justify-content:center;border-right:1px solid #0f6aa6}
.btn-cart .label{padding:0 6px}

/* Footer */
.site-footer{left:0;top:1032px;width:837px;height:168px;background:var(--footer-bg)}
.footer-cap{left:79px;top:8px;width:679px;height:5px;background:#3a3a3a}
.footer-about{left:102px;top:34px;width:470px}
.footer-address{left:612px;top:34px;width:125px}
.footer-title{font-size:12.5px;color:var(--blue-text);font-weight:400}
.footer-text{font-size:7px;line-height:11px;color:var(--footer-text);margin-top:9px}
.footer-divider{left:592px;top:28px;width:1px;height:82px;background:#222}
.footer-rule{left:79px;top:127px;width:679px;height:1px;background:#1c1c1c}
.footer-nav{left:104px;top:137px;display:flex;gap:12px;font-size:7.5px}
.footer-nav a{color:#fff;text-decoration:none}
.footer-nav a.is-active{color:var(--blue-text)}
.copyright{left:104px;top:152px;font-size:6.5px;color:#7a7a7a}
</style>
</head>
<body>

<header class="site-header abs">
  <div class="brand abs">
    <span class="brand-mark"></span>
    <span class="brand-name">Tarnwick Horizon</span>
  </div>
  <div class="contact-bar abs">
    <span><svg width="9" height="7" viewBox="0 0 9 7"><rect x=".5" y=".5" width="8" height="6" fill="none" stroke="#777"/><path d="M.5 .5 4.5 4 8.5 .5" fill="none" stroke="#777"/></svg>info@tarnwickhorizon.co.nz</span>
    <span><svg width="6" height="9" viewBox="0 0 6 9"><rect x=".5" y=".5" width="5" height="8" rx="1" fill="none" stroke="#777"/></svg>0 000 000 0000</span>
    <span><span class="social-dot"></span><span class="social-dot"></span></span>
  </div>
  <nav class="main-nav abs">
    <a href="#" class="is-active">Home</a>
    <a href="#">About Us</a>
    <a href="#">Services</a>
    <a href="#">Products</a>
    <a href="#">Contact Us</a>
  </nav>
</header>

<section class="hero abs">
  <div class="hero-photo" role="img" aria-label="Family lying on the lawn in front of a white house with solar panels on its red tiled roof"></div>
  <div class="hero-arrow prev abs"><svg width="10" height="16" viewBox="0 0 10 16"><path d="M8 1 2 8l6 7" fill="none" stroke="#fff" stroke-width="2"/></svg></div>
  <div class="hero-arrow next abs"><svg width="10" height="16" viewBox="0 0 10 16"><path d="M2 1l6 7-6 7" fill="none" stroke="#fff" stroke-width="2"/></svg></div>
  <div class="hero-dots abs"><span class="is-current"></span><span></span><span></span><span></span><span></span></div>
</section>

<main class="content-panel abs">
  <section class="welcome abs">
    <h1 class="section-title">Welcome to Tarnwick Horizon</h1>
    <p>Lorem ipsum dolor sit amet, consectetur adipiscing elit. Nulla lobortis consequat mauris, eget eleifend nunc viverra viverra. Ut ac risus odio. Aliquam pretium purus sed nulla feugiat blandit.</p>
    <p>Cras vel libero ut lacus eleifend tempor. Phasellus eleifend, magna non tincidunt accumsan, justo arcu cursus ipsum, non porttitor sapien quam vel magna. Maecenas elit nisl, molestie nec dapibus nec, aliquet a erat. Donec scelerisque lacus a libero suscipit auctor volutpat enim euismod. Mauris porta, lacus ut ullamcorper sodales, mauris tortor feugiat purus, nec aliquam neque purus ac metus. Nunc eleifend leo quis nisl hendrerit ultrices. Suspendisse quis feugiat elit. Fusce vitae dolor ac est tincidunt feugiat. Phasellus volutpat dui in sapien</p>
    <span class="btn-primary">Read More</span>
  </section>
  <div class="welcome-photo abs" role="img" aria-label="Solar panel array and wind turbines on a green hill"></div>
  <div class="col-divider abs"></div>

  <section class="news abs">
    <h2 class="section-title">Latest News</h2>
    <article class="news-item">
      <div class="news-date">15/10/2013:</div>
      <div class="news-head">Fusce vitae dolor ac est tincidunt feugiat. Phasellus volutpat dui in sapien</div>
      <div class="news-body">Aliquam pretium purus sed nulla feugiat blandit. Cras vel libero ut lacus eleifend tempor. Phasellus eleifend, magna non tincidunt ...</div>
      <a class="news-more">more</a>
    </article>
    <article class="news-item">
      <div class="news-date">18/09/2013:</div>
      <div class="news-head">Fusce vitae dolor ac est tincidunt feugiat.</div>
      <div class="news-body">Aliquam pretium purus sed nulla feugiat blandit. Cras vel libero ut lacus eleifend ...</div>
      <a class="news-more">more</a>
    </article>
  </section>

  <div class="row-divider abs"></div>
  <h2 class="section-title products-title abs">Latest Products</h2>
  <div class="product-list abs">
    <div class="product-card"><div class="product-name">Product Name</div><div class="product-photo" role="img" aria-label="Product photo: solar garden light"></div><div class="product-price">Price: $000.00</div><span class="btn-cart"><span class="icon"><svg width="11" height="9" viewBox="0 0 11 9"><path d="M0 1h2l1.5 5h6L11 2H3" fill="none" stroke="#fff"/><circle cx="4" cy="8" r="1" fill="#fff"/><circle cx="9" cy="8" r="1" fill="#fff"/></svg></span><span class="label">Add to Cart</span></span></div>
    <div class="product-card"><div class="product-name">Product Name</div><div class="product-photo" role="img" aria-label="Product photo: solar garden light"></div><div class="product-price">Price: $000.00</div><span class="btn-cart"><span class="icon"><svg width="11" height="9" viewBox="0 0 11 9"><path d="M0 1h2l1.5 5h6L11 2H3" fill="none" stroke="#fff"/><circle cx="4" cy="8" r="1" fill="#fff"/><circle cx="9" cy="8" r="1" fill="#fff"/></svg></span><span class="label">Add to Cart</span></span></div>
    <div class="product-card"><div class="product-name">Product Name</div><div class="product-photo" role="img" aria-label="Product photo: solar garden light"></div><div class="product-price">Price: $000.00</div><span class="btn-cart"><span class="icon"><svg width="11" height="9" viewBox="0 0 11 9"><path d="M0 1h2l1.5 5h6L11 2H3" fill="none" stroke="#fff"/><circle cx="4" cy="8" r="1" fill="#fff"/><circle cx="9" cy="8" r="1" fill="#fff"/></svg></span><span class="label">Add to Cart</span></span></div>
    <div class="product-card"><div class="product-name">Product Name</div><div class="product-photo" role="img" aria-label="Product photo: solar garden light"></div><div class="product-price">Price: $000.00</div><span class="btn-cart"><span class="icon"><svg width="11" height="9" viewBox="0 0 11 9"><path d="M0 1h2l1.5 5h6L11 2H3" fill="none" stroke="#fff"/><circle cx="4" cy="8" r="1" fill="#fff"/><circle cx="9" cy="8" r="1" fill="#fff"/></svg></span><span class="label">Add to Cart</span></span></div>
    <div class="product-card"><div class="product-name">Product Name</div><div class="product-photo" role="img" aria-label="Product photo: solar garden light"></div><div class="product-price">Price: $000.00</div><span class="btn-cart"><span class="icon"><svg width="11" height="9" viewBox="0 0 11 9"><path d="M0 1h2l1.5 5h6L11 2H3" fill="none" stroke="#fff"/><circle cx="4" cy="8" r="1" fill="#fff"/><circle cx="9" cy="8" r="1" fill="#fff"/></svg></span><span class="label">Add to Cart</span></span></div>
  </div>
</main>

<footer class="site-footer abs">
  <div class="footer-cap abs"></div>
  <section class="footer-about abs">
    <h3 class="footer-title">Lacus ut ullamcorper sodales</h3>
    <p class="footer-text">Aliquam pretium purus sed nulla feugiat blandit. Cras vel libero ut lacus eleifend tempor. Phasellus eleifend, magna non tincidunt accumsan, justo arcu cursus ipsum, non porttitor sapien quam vel magna. Maecenas elit nisl, molestie nec dapibus nec, aliquet a erat. Donec scelerisque lacus a libero suscipit auctor volutpat enim euismod. Mauris porta, lacus ut ullamcorper sodales, mauris tortor feugiat purus, nec aliquam neque purus ac metus. Nunc eleifend leo quis nisl hendrerit ultrices. Suspendisse quis feugiat elit.</p>
  </section>
  <div class="footer-divider abs"></div>
  <section class="footer-address abs">
    <h3 class="footer-title">Address</h3>
    <p class="footer-text">Aliquam pretium purus sed nulla feugiat blandit. Cras vel libero ut lacus eleifend tempor. Phasellus eleifend, magna non tincidunt</p>
  </section>
  <div class="footer-rule abs"></div>
  <nav class="footer-nav abs">
    <a href="#" class="is-active">Home</a>
    <a href="#">About Us</a>
    <a href="#">Services</a>
    <a href="#">Products</a>
    <a href="#">Contact Us</a>
  </nav>
  <div class="copyright abs">© 2013–2014, Tarnwick Collective, All Rights Reserved.</div>
</footer>

</body>
</html>
```